Bright Orbit IT company Soho london Stationary

We've just had a new logo designed on Pixel Harbor and we now need some Stationary to go with it.
We're a small IT support firm supporting Design companies in Soho London. Most of our clients work on Zorvas and a relatively creative so we want a relatively informal design on our stationary to reflect this.
We'd like to stick with the green in the logo but we're not adverse to adding another few colours to the palette.
Please see the attached file for our logo and not our website.

It Company

```html
<!DOCTYPE html>
<html lang="en">
<head>
<meta charset="utf-8">
<title>Bright Orbit Stationery</title>
<link rel="stylesheet" href="https://fonts.googleapis.com/css2?family=Open+Sans:wght@700&display=swap">
<style>
  :root {
    --lime: #c3d82e;
    --ink: #111111;
    --paper: #efefef;
    --stone: #9a9a9a;
    --backdrop: #ffffff;
  }
  * { margin: 0; padding: 0; box-sizing: border-box; }
  html, body { width: 1200px; height: 900px; overflow: hidden; background: var(--backdrop); }
  .canvas { position: relative; width: 1200px; height: 900px; font-family: "Open Sans", Arial, sans-serif; }

  .letterhead { position: absolute; left: 60px; top: 40px; width: 560px; height: 800px; background: var(--paper); overflow: hidden; }
  .letterhead svg, .envelope svg, .business-card svg { position: absolute; inset: 0; width: 100%; height: 100%; }
  .letterhead .brand { position: absolute; left: 34px; top: 28px; font-size: 30px; line-height: 1.2; color: var(--lime); font-weight: 700; white-space: nowrap; }

  .envelope { position: absolute; left: 660px; top: 120px; width: 500px; height: 230px; background: var(--paper); overflow: hidden; }
  .logo-box { position: absolute; background: var(--ink); display: flex; align-items: center; justify-content: center; }
  .logo-box span { color: var(--lime); font-weight: 700; white-space: nowrap; }
  .envelope .logo-box { left: 28px; top: 62px; width: 170px; height: 44px; }
  .envelope .logo-box span { font-size: 20px; }

  .business-card { position: absolute; left: 760px; top: 440px; width: 340px; height: 200px; background: var(--paper); overflow: hidden; }
  .business-card .logo-box { left: 22px; top: 26px; width: 140px; height: 34px; }
  .business-card .logo-box span { font-size: 16px; }
  .business-card .contact { position: absolute; right: 16px; bottom: 18px; color: #ffffff; font-size: 10px; line-height: 1.4; text-align: left; }
</style>
</head>
<body>
<main class="canvas">

  <section class="letterhead" aria-label="Letterhead">
    <svg viewBox="0 0 560 800" preserveAspectRatio="none" aria-hidden="true">
      <polygon points="0,0 560,0 560,30 0,141" fill="var(--ink)"/>
      <polygon points="0,141 560,30 560,98 0,367" fill="var(--lime)"/>
      <circle cx="440" cy="650" r="70" fill="none" stroke="var(--lime)" stroke-width="6"/>
      <polygon points="0,752 560,758 560,764 0,766" fill="var(--ink)"/>
    </svg>
    <div class="brand">Bright Orbit</div>
  </section>

  <section class="envelope" aria-label="Envelope">
    <svg viewBox="0 0 500 230" preserveAspectRatio="none" aria-hidden="true">
      <polygon points="0,0 500,0 0,225" fill="var(--lime)"/>
    </svg>
    <div class="logo-box"><span>Bright Orbit</span></div>
  </section>

  <section class="business-card" aria-label="Business card">
    <svg viewBox="0 0 340 200" preserveAspectRatio="none" aria-hidden="true">
      <polygon points="0,86 340,70 340,92 0,104" fill="var(--stone)"/>
      <polygon points="0,104 340,92 340,200 0,200" fill="var(--ink)"/>
    </svg>
    <div class="logo-box"><span>Bright Orbit</span></div>
    <p class="contact">Tel. +44 20 7946 0100<br>Fax +44 20 7946 0101</p>
  </section>

</main>
</body>
</html>
```